Create a new email template des

We are looking for 2 email template designed similar to the attached supplied like Inn Midnight in order to promote of photography business and also our marketing agency.

Both similar in design and branding but with a slight change to the body area.

1. Email is to show images and a little text as attached.
2. Email is to show more text and longer emails with tips and best practices education.

Our website is: www.brookmerestudio.example

The photography site is: http://brookmerestudio.example/hotel-photography/

Target Market(s)

Luxury Hotels

Industry/Entity Type

Business

Requirements
Must have
• Stylish design and as per breif

```html
<!DOCTYPE html>
<html lang="en">
<head>
<meta charset="utf-8">
<title>Brookmere Studio – Holiday Email</title>
<link href="https://fonts.googleapis.com/css2?family=Montserrat:wght@300;400;500;600&display=swap" rel="stylesheet">
<style>
:root{
  --page:#f1f1f1;
  --paper:#ffffff;
  --ink:#333333;
  --muted:#777777;
  --red:#e0112b;
  --dark:#262626;
  --line:#d9d9d9;
}
*{box-sizing:border-box;margin:0;padding:0}
html,body{width:1200px;height:3056px;overflow:hidden}
body{background:var(--page);font-family:"Montserrat",Arial,sans-serif;color:var(--ink);position:relative}
.abs{position:absolute}
.center{text-align:center}
.preheader{top:100px;left:0;width:1200px;font-size:15px;color:var(--muted)}
.preheader a{color:var(--red);text-decoration:none}
.email{top:152px;left:192px;width:800px;height:2892px;background:var(--paper);box-shadow:0 0 10px rgba(0,0,0,.08)}
.header{top:0;left:0;width:800px;height:176px;background:var(--dark)}
.brand{top:66px;left:44px;color:#fff;font-size:30px;font-weight:400;letter-spacing:1px;text-transform:uppercase}
.nav{top:64px;right:40px;display:flex;gap:12px}
.nav span{border:2px solid #8a8a8a;color:#ddd;font-size:15px;padding:12px 16px}
.hero{top:176px;left:0;width:800px;height:404px;background:linear-gradient(180deg,#1f2a45 0%,#3b4660 45%,#6a5a3e 80%,#2a2418 100%)}
.hero-title{top:338px;left:0;width:800px;color:#fff;font-size:36px;font-weight:400;line-height:42px}
.btn{display:inline-block;background:var(--red);color:#fff;font-size:16px;font-weight:500;padding:0 32px;height:58px;line-height:58px}
.btn::after{content:" ›"}
.hero-btn{top:480px;left:0;width:800px}
.h2{font-size:33px;font-weight:400;color:#333}
.body-text{font-size:14px;line-height:21px;color:#666}
.ready-title{top:624px;left:0;width:800px}
.ready-text{top:672px;left:90px;width:620px}
.ready-btn{top:740px;left:0;width:800px}
.rates-img{top:830px;left:140px;width:256px;height:256px;border-radius:50%;background:radial-gradient(circle at 55% 55%,#ffffff 0%,#e8e8e8 60%,#d6d6d6 100%)}
.price{top:818px;left:104px;width:140px;height:140px;border-radius:50%;background:var(--red);color:#fff;font-size:44px;font-weight:400;line-height:140px;text-align:center}
.rates-title{top:884px;left:432px;width:320px;font-size:34px;line-height:40px}
.rates-text{top:976px;left:432px;width:330px}
.mark{top:1150px;left:384px;width:32px;height:32px;border:2px solid #222}
.choose{top:1200px;left:0;width:800px;font-size:22px;font-weight:500}
.card{width:296px}
.card .photo{width:296px;height:252px}
.card .badge{position:absolute;left:-12px;top:214px;width:84px;height:84px;border-radius:50%;background:var(--red);color:#fff;font-size:14px;font-weight:600;line-height:84px;text-align:center}
.card .name{position:absolute;left:88px;top:258px;width:210px;font-size:21px;color:#555;line-height:26px}
.c1{top:1276px;left:80px}.c2{top:1276px;left:448px}
.c3{top:1648px;left:80px}.c4{top:1648px;left:448px}
.p1{background:linear-gradient(180deg,#9cc3de 0%,#c8b79a 55%,#3fa6c6 100%)}
.p2{background:linear-gradient(180deg,#e8a66a 0%,#b9826a 50%,#5f4a44 100%)}
.p3{background:linear-gradient(180deg,#6c6f86 0%,#a0543a 55%,#3c2a22 100%)}
.p4{background:linear-gradient(180deg,#d39a55 0%,#8a5a34 55%,#3a2a20 100%)}
.more-btn{top:2020px;left:0;width:800px}
.friend{top:2128px;left:36px;width:728px;height:290px;background:linear-gradient(180deg,#3a3a32 0%,#2a2a24 100%)}
.friend-title{top:36px;left:0;width:728px;color:#fff;font-size:30px;font-weight:400}
.friend-text{top:92px;left:54px;width:620px;color:#ddd}
.friend-btn{top:168px;left:0;width:728px}
.social{top:2456px;left:0;width:800px;display:flex;justify-content:center;gap:8px}
.social i{width:40px;height:40px;border-radius:50%;display:block}
.contact{top:2524px;left:0;width:800px;font-size:15px;line-height:24px;color:#555}
.divider{top:2604px;left:120px;width:560px;height:1px;background:var(--line)}
.pin{top:2588px;left:386px;width:28px;height:32px;background:var(--paper)}
.addr{top:2628px;width:260px;font-size:14px;line-height:22px;color:#666}
.addr b{display:block;color:#333;font-weight:600}
.addr-1{left:180px}.addr-2{left:436px}
.foot-line{top:2750px;left:120px;width:560px;height:1px;background:var(--line)}
.foot-mark{top:2770px;left:56px;width:64px;height:64px;border:2px solid #e2e2e2}
.copy{top:2792px;left:0;width:800px;font-size:15px;color:#666}
.redbar{top:2872px;left:0;width:800px;height:14px;background:var(--red)}
</style>
</head>
<body>
<p class="abs preheader center">For anything about this mail you can contact us by <a href="#">click this link</a>.</p>

<main class="abs email">
  <header class="abs header">
    <div class="abs brand">Brookmere Studio</div>
    <nav class="abs nav"><span>Favorites</span><span>Refer</span><span>Book Now</span></nav>
  </header>

  <section class="abs hero" role="img" aria-label="Luxury resort pavilion lit at dusk beside a pool"></section>
  <h1 class="abs hero-title center">Visit With Family<br>and<br>Stay with Us</h1>
  <div class="abs hero-btn center"><span class="btn">Come Website for more</span></div>

  <h2 class="abs h2 ready-title center">Ready for The Holiday Weekend?</h2>
  <p class="abs body-text ready-text center">Lorem ipsum dolor sit amet, consectetur adipiscing elit, sed do eiusmod tempor incididunt ut labore et dolore magna aliqua. Ut enim ad minim veniam.</p>
  <div class="abs ready-btn center"><span class="btn">Book Now</span></div>

  <div class="abs rates-img" role="img" aria-label="Hand holding a smartphone showing a booking app"></div>
  <div class="abs price">$129</div>
  <h2 class="abs h2 rates-title">Find the Best Holiday Rates</h2>
  <p class="abs body-text rates-text">Lorem ipsum dolor sit amet, consectetur adipiscing elit, sed do eiusmod tempor incididunt ut labore et dolore magna aliqua. Ut enim ad minim veniam.</p>

  <div class="abs mark"></div>
  <h3 class="abs choose center">Choose Your Perfect Location with off Rates</h3>

  <article class="abs card c1"><div class="photo p1" role="img" aria-label="Hotel pool terrace with palm trees"></div><div class="badge">$100 off</div><div class="name">Saltmarsh Hotel</div></article>
  <article class="abs card c2"><div class="photo p2" role="img" aria-label="Beachfront resort at sunset"></div><div class="badge">$100 off</div><div class="name">Saltmarsh Dunes</div></article>
  <article class="abs card c3"><div class="photo p3" role="img" aria-label="Palace terrace with lounge seating at dusk"></div><div class="badge">$100 off</div><div class="name">Orchard Court Terrace</div></article>
  <article class="abs card c4"><div class="photo p4" role="img" aria-label="Warmly lit restaurant courtyard with dining tables"></div><div class="badge">$100 off</div><div class="name">Lantern Bay<br>Restaurant</div></article>

  <div class="abs more-btn center"><span class="btn">See More to Book Now</span></div>

  <section class="abs friend" role="img" aria-label="Dark textured dining scene behind the referral offer">
    <h2 class="abs friend-title center">Friend with Benefits</h2>
    <p class="abs body-text friend-text center">Lorem ipsum dolor sit amet, consectetur adipiscing elit, sed do eiusmod tempor incididunt ut labore et dolore magna aliqua. Ut enim ad minim veniam.</p>
    <div class="abs friend-btn center"><span class="btn">Share your code</span></div>
  </section>

  <div class="abs social"><i style="background:#3b5998"></i><i style="background:#1da1f2"></i><i style="background:#0077b5"></i><i style="background:#dd4b39"></i></div>
  <p class="abs contact center">P: +000 555 0172<br>E: info@brookmerestudio.example</p>

  <div class="abs divider"></div>
  <svg class="abs pin" viewBox="0 0 28 32"><path d="M14 2a9 9 0 0 0-9 9c0 7 9 18 9 18s9-11 9-18a9 9 0 0 0-9-9z" fill="#e0112b"/><circle cx="14" cy="11" r="3.5" fill="#fff"/></svg>
  <p class="abs addr addr-1"><b>Dubai address</b>12 Harbour Walk, Dubai</p>
  <p class="abs addr addr-2"><b>London Address</b>40 Wren Row, London, EC0 1AA</p>

  <div class="abs foot-line"></div>
  <div class="abs foot-mark"></div>
  <p class="abs copy center">Copyright Northgate Build Co 2016</p>
  <div class="abs redbar"></div>
</main>
</body>
</html>
```